Manufacturer's Representative Group needs a clean new Website

We represent and sell a number of suppliers that design and build products used in Biopharmaceutical manufacturing. Our sales region is in the central US. Our customer base is scientific / engineering based - so clean, we organized design with a focus on the products - easy and clear navigation is necessary. We do not sell direct or warehouse product - so e-commerce is not needed. Our customers will use the website for reference on what we do and offer - we will use the site as a platform to present products from each vendor and the home page will be used to capture an overview and draw users deeper into the site. You can view our current site - which needs A LOT of help to get ideas on products represented and types of products

Target Market(s)

Engineers and Pharmaceutical / Bio pharm end users

Industry/Entity Type

E-Commerce

Number of Pages Required

2 page

Font styles to use
Sans Serif

Requirements
Must have
• I need a home page that provides a snapshot of my company and the product lines we represent - then a second page that I can copy as a template for each line I rep as well as for an "About us / contact" page.
• I would like to be able to manage content on the pages so something easy to adjust pictures or add content is a must
• Must use our logo

```html
<!DOCTYPE html>
<html lang="en">
<head>
<meta charset="utf-8">
<title>Prairie Bio – Biopharmaceutical Products</title>
<link rel="stylesheet" href="https://fonts.googleapis.com/css2?family=Open+Sans:ital,wght@0,400;0,600;0,700;1,400&display=swap">
<style>
:root{
  --dark:#2d3038;
  --nav:#30343c;
  --navline:#40444c;
  --orange:#ee7421;
  --navy:#14246b;
  --text:#444;
  --muted:#666;
  --light:#f1f1f1;
  --footer:#141414;
  --footer-text:#a9a9a9;
  --white:#fff;
}
*{box-sizing:border-box;margin:0;padding:0}
html,body{width:701px;height:1200px;overflow:hidden}
body{position:relative;font-family:"Open Sans",Arial,sans-serif;color:var(--text);background:var(--white)}
.abs{position:absolute}

.topbar{left:0;top:0;width:701px;height:22px;background:var(--dark);color:#e6e6e6;font-size:7.2px}
.topbar .contact{left:77px;top:6px;display:flex;gap:6px;align-items:center}
.topbar .contact svg{width:8px;height:8px;fill:#ddd}
.topbar .links{right:77px;top:6px;display:flex;gap:13px}

.header{left:0;top:22px;width:701px;height:64px}
.brand{display:flex;align-items:center;gap:7px}
.brand .dot{width:14px;height:14px;border-radius:50%;background:var(--orange)}
.brand .name{font-size:21px;color:var(--navy);font-weight:400}
.header .brand{left:77px;top:18px}
.search{left:480px;top:21px;width:144px;height:19px;border:1px solid #ccc;display:flex}
.search span{flex:1;font-size:7px;color:#999;padding:4px 9px}
.search b{width:20px;background:var(--orange);display:flex;align-items:center;justify-content:center}

.nav{left:0;top:86px;width:701px;height:37px;background:var(--nav)}
.nav ul{position:absolute;left:77px;top:0;width:546px;height:37px;display:flex;list-style:none;border-left:1px solid var(--navline)}
.nav li{height:37px;border-right:1px solid var(--navline);color:#eee;font-size:7px;display:flex;align-items:center;justify-content:center}

.hero{left:0;top:123px;width:701px;height:293px;
  background:
    radial-gradient(ellipse 170px 140px at 330px 110px,rgba(232,210,196,.75),rgba(232,210,196,0) 70%),
    radial-gradient(ellipse 120px 240px at 460px 170px,rgba(240,244,248,.8),rgba(240,244,248,0) 70%),
    radial-gradient(ellipse 260px 230px at 590px 180px,rgba(226,232,240,.95),rgba(226,232,240,0) 75%),
    radial-gradient(ellipse 200px 150px at 120px 60px,rgba(98,124,152,.6),rgba(98,124,152,0) 70%),
    linear-gradient(100deg,#4a6480 0%,#6f87a1 30%,#a9b7c7 55%,#d4dbe3 80%,#e5e9ee 100%)}
.hero h1{position:absolute;left:77px;top:63px;color:#fff;font-weight:400;line-height:1.03;font-size:27px;letter-spacing:.5px}
.hero h1 span{display:block;font-size:33px}
.hero .sub{left:77px;top:133px;color:var(--orange);font-size:13px;font-weight:600}
.hero .btn{left:77px;top:164px;width:89px;height:32px;background:#3a3d43;color:#fff;font-size:10px;display:flex;align-items:center;justify-content:center}

.feature{top:433px;width:174px;height:134px;border:1px solid #d4d4d4}
.feature .img{height:89px}
.feature .bar{height:44px;background:var(--orange);color:#fff;padding:8px 14px;position:relative}
.feature small{display:block;font-size:7px;opacity:.9}
.feature strong{display:block;font-size:13px;font-weight:400;margin-top:1px}
.feature svg{position:absolute;right:10px;top:13px;width:17px;height:17px}

.tabs{left:77px;top:586px;width:547px;height:34px;background:var(--dark);display:flex;font-size:10px;font-weight:700;color:#fff}
.tabs div{display:flex;align-items:center;padding:0 12px}
.tabs .active{width:78px;background:var(--orange);justify-content:center;padding:0;margin-right:8px}

.card{top:636px;width:128px;height:186px;background:#f5f5f5;border:1px solid #e0e0e0;text-align:center;box-shadow:0 6px 5px -4px rgba(0,0,0,.25)}
.card .img{margin:6px 6px 0;height:80px}
.card h3{font-size:7.6px;font-weight:700;color:#333;margin-top:11px}
.card p{font-size:6.8px;line-height:13px;color:var(--muted);margin-top:3px}
.card .more{display:inline-block;margin-top:9px;background:var(--navy);color:#fff;font-size:7px;padding:4px 9px}

.partners{left:0;top:852px;width:701px;height:142px;background:var(--light)}
.partners h2{position:absolute;left:0;width:701px;top:20px;text-align:center;font-size:10px;font-weight:600;color:#333}
.partner{top:46px;width:104px;height:68px;background:#fff;border:1px solid #d6d6d6;display:flex;align-items:center;justify-content:center;font-size:9.5px;font-weight:700;color:#2d4d8a}

.footer{left:0;top:994px;width:701px;height:206px;background:var(--footer);color:var(--footer-text);font-size:7px}
.footer .brand{left:77px;top:28px}
.footer .brand .name{color:#fff;font-size:16px}
.footer .brand .dot{width:11px;height:11px}
.footer h4{font-size:9px;font-weight:600;color:#ddd;padding-bottom:8px;border-bottom:1px solid #444;width:115px}
.footer .about{left:77px;top:62px;width:128px;line-height:13px}
.col{top:24px}
.tweet{display:flex;gap:6px;margin-top:10px;line-height:14px}
.tweet i{font-style:italic;display:block}
.info{display:flex;gap:6px;align-items:center;margin-top:13px}
.info svg{width:9px;height:9px;fill:#999;flex:none}
.input{width:122px;height:15px;background:#fff;border:1px solid #ccc;color:#555;font-size:6.8px;padding:2px 8px;margin-top:7px}
.login{display:inline-block;margin-top:7px;background:var(--navy);color:#fff;padding:5px 10px;font-size:7px;font-weight:600}
.footer .rule{left:77px;top:160px;width:547px;height:1px;background:#444}
.footer .copy{left:77px;top:174px}
.social{left:529px;top:173px;display:flex;gap:4px}
.social span{width:16px;height:16px;border-radius:50%;background:#fff}
</style>
</head>
<body>

<div class="abs topbar">
  <div class="abs contact">
    <svg viewBox="0 0 10 10"><path d="M2 0l2 2-1 1.5c.7 1.4 1.6 2.3 3 3L7.5 5.5 10 7.5 8.5 10C4 9.5.5 6 0 1.5z"/></svg>
    <span>Call us: (0800) 555 014-2290</span>
    <svg viewBox="0 0 10 8"><path d="M0 0h10v8H0zM1 1l4 3 4-3z" fill-rule="evenodd"/></svg>
    <span>Email: hello@prairiebiorep.com</span>
  </div>
  <div class="abs links"><span>Home</span><span>Contact</span><span>Sitemap</span></div>
</div>

<header class="abs header">
  <div class="abs brand"><span class="dot"></span><span class="name">Prairie Bio</span></div>
  <div class="abs search"><span>Search</span><b><svg width="9" height="9" viewBox="0 0 10 10"><circle cx="4" cy="4" r="3" fill="none" stroke="#fff" stroke-width="1.5"/><path d="M6.3 6.3L9 9" stroke="#fff" stroke-width="1.6"/></svg></b></div>
</header>

<nav class="abs nav">
  <ul>
    <li style="width:87px">HOME</li>
    <li style="width:88px">PRODUCTS</li>
    <li style="width:94px">ABOUT US</li>
    <li style="width:103px">SUPPORET</li>
    <li style="width:71px">BLOG</li>
    <li style="width:103px">CONTACT &nbsp;US</li>
  </ul>
</nav>

<section class="abs hero" role="img" aria-label="Scientist in a lab coat holding a model of a DNA double helix">
  <h1>OFFERING<span>THE HIGHEST</span></h1>
  <div class="abs sub">QUALITY CONTACT PRODUCT</div>
  <div class="abs btn">VIEW MORE !</div>
</section>

<div class="abs feature" style="left:77px">
  <div class="img" role="img" aria-label="Clear plastic media bottles" style="background:radial-gradient(ellipse 45px 38px at 50% 55%,#b4bcd0,rgba(180,188,208,0) 80%),linear-gradient(#bfe0f3,#f2faff)"></div>
  <div class="bar"><small>MEETING USP</small><strong>788 PARTICULATE</strong>
    <svg viewBox="0 0 20 20"><circle cx="8" cy="8" r="6" fill="none" stroke="#fff" stroke-width="2.5"/><path d="M12.5 12.5L18 18" stroke="#fff" stroke-width="3"/></svg></div>
</div>
<div class="abs feature" style="left:264px">
  <div class="img" role="img" aria-label="Square clear plastic bottle" style="background:radial-gradient(ellipse 32px 40px at 50% 55%,#c6cbd3,rgba(198,203,211,0) 80%),linear-gradient(#bfe0f3,#f2faff)"></div>
  <div class="bar"><small>MEETING USP</small><strong>788 PARTICULATE</strong>
    <svg viewBox="0 0 20 20"><circle cx="8" cy="8" r="6" fill="none" stroke="#fff" stroke-width="2.5"/><path d="M12.5 12.5L18 18" stroke="#fff" stroke-width="3"/></svg></div>
</div>
<div class="abs feature" style="left:450px">
  <div class="img" role="img" aria-label="Single-use bioprocess bags with tubing" style="background:radial-gradient(ellipse 80px 40px at 50% 65%,#f6f9fc,rgba(246,249,252,0) 80%),linear-gradient(#a9d3ee,#e9f5fc)"></div>
  <div class="bar"><small>MEETING USP</small><strong>788 PARTICULATE</strong>
    <svg viewBox="0 0 20 20"><circle cx="8" cy="8" r="6" fill="none" stroke="#fff" stroke-width="2.5"/><path d="M12.5 12.5L18 18" stroke="#fff" stroke-width="3"/></svg></div>
</div>

<div class="abs tabs">
  <div class="active">POPULAR</div><div>NEW ARRIVALS</div><div>NON RECUSANDAE</div>
</div>

<article class="abs card" style="left:77px">
  <div class="img" role="img" aria-label="Cleanroom equipment cabinet" style="background:radial-gradient(ellipse 40px 34px at 55% 55%,#eef0f2,rgba(238,240,242,0) 85%),linear-gradient(#3a3f46,#9aa1a9 45%,#dfe3e7)"></div>
  <h3>Aseptic Valves</h3>
  <p>Sed ut perspiciatis unde omnis<br>iste natus error sit voluptatem<br>accusantium doloremque</p>
  <span class="more">Read More</span>
</article>
<article class="abs card" style="left:216px">
  <div class="img" role="img" aria-label="Red peristaltic pump" style="background:radial-gradient(ellipse 40px 30px at 75% 55%,#9a9a96,rgba(154,154,150,0) 85%),linear-gradient(120deg,#c8242a,#a51d22 50%,#e2d2b4)"></div>
  <h3>Aseptic Valves</h3>
  <p>Sed ut perspiciatis unde omnis<br>iste natus error sit voluptatem<br>accusantium doloremque</p>
  <span class="more">Read More</span>
</article>
<article class="abs card" style="left:355px">
  <div class="img" role="img" aria-label="Blue peristaltic pump with tubing" style="background:radial-gradient(ellipse 36px 30px at 55% 62%,#4c4f55,rgba(76,79,85,0) 85%),linear-gradient(120deg,#2a5bb5,#3c6fc8 45%,#d8c8a6)"></div>
  <h3>Aseptic Valves</h3>
  <p>Sed ut perspiciatis unde omnis<br>iste natus error sit voluptatem<br>accusantium doloremque</p>
  <span class="more">Read More</span>
</article>
<article class="abs card" style="left:496px">
  <div class="img" role="img" aria-label="Silicone fittings and tubing connectors" style="background:radial-gradient(ellipse 50px 30px at 50% 65%,#c9d3df,rgba(201,211,223,0) 85%),linear-gradient(#1f3a66,#5b78a2 60%,#9db0c9)"></div>
  <h3>Aseptic Valves</h3>
  <p>Sed ut perspiciatis unde omnis<br>iste natus error sit voluptatem<br>accusantium doloremque</p>
  <span class="more">Read More</span>
</article>

<section class="abs partners">
  <h2>COMPANIES REPRESENTED</h2>
  <div class="abs partner" style="left:77px">Cleanway</div>
  <div class="abs partner" style="left:187px">Norbridge Polymers</div>
  <div class="abs partner" style="left:297px">Hollis Pumps</div>
  <div class="abs partner" style="left:408px">Veritune</div>
  <div class="abs partner" style="left:519px">Coilflex Tubing Co.</div>
</section>

<footer class="abs footer">
  <div class="abs brand"><span class="dot"></span><span class="name">Prairie Bio</span></div>
  <p class="abs about">At vero eos et accusamus et iusto odio dignissimos ducimus qui blan-ditiis praesentium voluptatum del-eniti atque corrupti quos dolores et quas molestias</p>

  <div class="abs col" style="left:216px">
    <h4>TWITTER &nbsp;FEED</h4>
    <div class="tweet"><span>●</span><div>Sed ut perspiciatis unde omnis<br>iste natus error sit voluptatem<i>March 10,2014</i></div></div>
    <div class="tweet"><span>●</span><div>Sed ut perspiciatis unde omnis<br>iste natus error sit voluptatem<i>March 10,2014</i></div></div>
  </div>

  <div class="abs col" style="left:356px">
    <h4>CONTACT INFO</h4>
    <div class="info"><svg viewBox="0 0 10 10"><path d="M5 0L0 4h1.5v6h7V4H10z"/></svg>Address: 123 Street, City, Country</div>
    <div class="info" style="margin-top:17px"><svg viewBox="0 0 10 10"><path d="M2 0l2 2-1 1.5c.7 1.4 1.6 2.3 3 3L7.5 5.5 10 7.5 8.5 10C4 9.5.5 6 0 1.5z"/></svg>Phone: (123) 456-7890</div>
    <div class="info" style="margin-top:17px"><svg viewBox="0 0 10 10"><path d="M2 0h6v3H2zM0 3h10v5H8v2H2V8H0z"/></svg>Fax: (123) 456-7890</div>
    <div class="info" style="margin-top:17px"><svg viewBox="0 0 10 8"><path d="M0 0h10v8H0zM1 1l4 3 4-3z" fill-rule="evenodd"/></svg>Email: &nbsp;<span style="color:#ddd">info@yoursite.com</span></div>
  </div>

  <div class="abs col" style="left:498px">
    <h4 style="width:125px">NEWS LETTER</h4>
    <p style="margin-top:9px;line-height:13px">Sign up for our newsletter and get<br>the latest news.</p>
    <div class="input">User &nbsp;name</div>
    <div class="input">Password</div>
    <span class="login">Login</span>
  </div>

  <div class="abs rule"></div>
  <div class="abs copy">© &nbsp; Prairie Bio Representatives 2014 • Privacy Policy</div>
  <div class="abs social"><span></span><span></span><span></span><span></span><span></span></div>
  <div class="abs" style="left:661px;top:174px">C12</div>
</footer>

</body>
</html>
```